Site for company producing and selling products for children's health

We need an appealing professional web site design and images for a brand new company producing and selling products focused on children’s health. The site will offer information to visitors on the company, the company’s products, and general resources related to children’s health. Additionally the site will offer e-commerce functionality to allow for ordering of the company’s products.
The content and navigation for the site will be generated by programming, such as php or asp, and therefore any images used in the navigation portions of the site should allow for HTML markup to be overlaid rather than having the text built into the image or graphic.
The design must include 2 layouts, one for the landing/home page that includes only top navigation, and an inner page layout that includes both top and left navigation.
The header area of the site should include a place for links to access the visitor’s cart and profile similar to the top sections of quillbarn.com, tervodo.com, and pikmart.com.
The landing page of the site should include some type of “changing” image area where we can include multiple image files for rotation to visitors similar to what is seen at vorlo.com or mallowkite.com. The flash/animation mechanism does not need to be provided (although it would be a plus if it was) but the design must accommodate the space for it.
The company’s colors are Orange (FF9900) and Blue (0066FF) and the logo can be viewed at http://corvanelkids.com/logo.png
All CSS and markup provided must be display consistently in Internet Explorer 7+, FifeFox, Google Chrome, and Safari.
Incorporating social media links (facebook, twitter, etc.) is desirable.
Target Market(s)
Parents who are conscious of health risks associated with children's diets and consumer food products.
Industry/Entity Type
E-Commerce
Look and feel
Each slider illustrates characteristics of the customer's brand and the style your logo design should communicate.

```html
<!DOCTYPE html>
<html lang="en">
<head>
<meta charset="utf-8">
<title>Corvanel Kids – Inner Page</title>
<link href="https://fonts.googleapis.com/css2?family=Arimo:ital,wght@0,400;0,700;1,700&display=swap" rel="stylesheet">
<style>
:root{
  --orange:#ff9900;
  --orange-light:#ffae42;
  --blue:#0066ff;
  --blue-band:#2a86dc;
  --blue-band-dark:#1f74cf;
  --text:#6b6b6b;
  --text-dark:#222;
  --muted:#999;
  --rule:#d8d8d8;
  --bg:#ffffff;
}
*{box-sizing:border-box;margin:0;padding:0}
html,body{width:1200px;height:1084px;overflow:hidden;background:var(--bg)}
body{font-family:"Arimo",Arial,sans-serif;color:var(--text);position:relative}
a{text-decoration:none;color:inherit}
.page{position:absolute;left:0;top:0;width:1200px;height:1084px}
.top-rule{position:absolute;left:44px;top:70px;width:1112px;height:4px;background:var(--orange)}

/* Utility links */
.account-bar{position:absolute;top:89px;left:788px;display:flex;align-items:center;font-size:14px;color:var(--text-dark)}
.account-bar .sep{margin:0 20px;color:#555}
.account-bar .cart{display:flex;align-items:center;gap:8px}
.account-bar .cart svg{display:block}
.account-bar .count{margin-left:14px}

/* Brand */
.brand{position:absolute;left:94px;top:150px;display:flex;align-items:center;gap:10px}
.brand .dot{width:22px;height:22px;border-radius:50%;background:var(--blue)}
.brand .name{font-weight:700;font-size:28px;color:var(--orange);letter-spacing:-0.5px}

/* Main nav */
.main-nav{position:absolute;top:174px;left:0;height:35px}
.main-nav a{position:absolute;top:0;height:35px;background:#fff;border-radius:3px 3px 0 0;
  box-shadow:0 -1px 6px rgba(0,0,0,.18);font-size:16px;color:var(--text-dark);
  display:flex;align-items:center;justify-content:center}

/* Title band */
.title-band{position:absolute;left:44px;top:209px;width:1112px;height:59px;
  background:linear-gradient(100deg,var(--blue-band-dark) 0%,var(--blue-band) 40%,#3d8fe2 70%,#4a90e6 100%)}
.title-band h1{position:absolute;left:270px;top:14px;font-weight:400;font-size:28px;color:#fff}
.title-fade{position:absolute;left:44px;top:268px;width:1112px;height:38px;background:linear-gradient(#e6e6e6,#fff)}

/* Side nav */
.side-nav{position:absolute;left:56px;top:303px;width:222px;list-style:none;border-top:1px solid var(--rule)}
.side-nav li{height:35px;border-bottom:1px solid var(--rule);display:flex;align-items:center;font-size:14px;color:var(--text)}
.side-nav li::before{content:"";width:7px;height:7px;border-radius:50%;background:#aaa;margin:0 20px 0 9px}
.side-nav li.active{color:var(--blue)}
.side-nav li.active::before{background:var(--blue)}

/* Content */
.content{position:absolute;left:314px;top:299px;width:560px;font-size:14px;line-height:21px;color:var(--text)}
.content p{margin-bottom:21px}
.content .link{color:var(--blue)}
.content h2{font-size:14px;font-weight:700;color:var(--text-dark);line-height:21px}
.content ul{list-style:none;margin:0 0 20px;}
.content li{position:relative;padding-left:18px;line-height:24.5px}
.content li::before{content:"";position:absolute;left:0;top:9px;width:6px;height:6px;background:var(--blue)}

/* Aside */
.aside{position:absolute;left:933px;top:305px;width:223px}
.photo{width:223px;height:144px;background:linear-gradient(160deg,#9fd3f2 0%,#7fb34a 45%,#e2c3a0 75%,#5f8a3a 100%)}
.enlarge{margin-top:8px;display:flex;align-items:center;gap:6px;font-size:12px;font-weight:700;font-style:italic;color:#777;padding-left:10px}
.aside .rule{margin-top:36px;height:4px;background:var(--orange)}
.aside h3{margin-top:34px;font-size:21px;font-weight:700;color:var(--blue)}
.aside .intro{margin-top:18px;font-size:14px;line-height:21px;color:var(--text)}
.field{display:block;width:210px;height:23px;border:1px solid #cfcfcf;font-size:12px;color:#999;padding:4px 12px;font-family:inherit}
.field.name{margin-top:30px}
.field.email{margin-top:29px}
.btn-subscribe{position:absolute;left:106px;top:464px;width:104px;height:25px;background:var(--orange-light);color:#fff;font-size:16px;display:flex;align-items:center;justify-content:center}

/* Footer */
.footer-rule{position:absolute;left:44px;top:866px;width:1112px;height:4px;background:var(--orange)}
.footer-col{position:absolute;top:903px}
.footer-col h4{font-size:17px;font-weight:700;color:var(--muted);margin-bottom:10px}
.footer-col ul{list-style:none}
.footer-col li{font-size:14px;line-height:23.5px;color:var(--muted);display:flex;align-items:center}
.footer-col li svg{margin-right:13px}
.contact{position:absolute;top:938px;font-size:14px;line-height:21px;color:var(--muted)}
.footer-brand{position:absolute;left:1012px;top:956px;font-size:18px;font-weight:700;color:#b8b8b8}
.legal{position:absolute;top:1037px;left:68px;font-size:13.5px;color:var(--muted)}
.footer-nav{position:absolute;top:1037px;left:349px;font-size:13.5px;color:var(--muted)}
.footer-nav .sep{margin:0 14px}
.social{position:absolute;left:1006px;top:1034px;display:flex;gap:3px}
.social span{width:21px;height:21px;border-radius:3px;background:#a9a9a9}
</style>
</head>
<body>
<div class="page">
  <div class="top-rule"></div>

  <div class="account-bar">
    <a href="#">My Account</a><span class="sep">|</span>
    <a href="#">Order Status</a><span class="sep">|</span>
    <a href="#" class="cart">
      <svg width="17" height="15" viewBox="0 0 17 15" aria-hidden="true"><path d="M0 1h3l2.5 8h8.5l2-6H4.3" fill="none" stroke="#222" stroke-width="2"/><circle cx="6.5" cy="13" r="1.6" fill="#222"/><circle cx="13" cy="13" r="1.6" fill="#222"/></svg>
      Cart</a>
    <span class="count">0 Items</span>
  </div>

  <a href="#" class="brand"><span class="dot"></span><span class="name">corvanelkids</span></a>

  <nav class="main-nav">
    <a href="#" style="left:407px;width:94px">Home</a>
    <a href="#" style="left:513px;width:117px">About us</a>
    <a href="#" style="left:641px;width:94px">News</a>
    <a href="#" style="left:746px;width:117px">Products</a>
    <a href="#" style="left:875px;width:117px">Services</a>
    <a href="#" style="left:1004px;width:105px">Contact</a>
  </nav>

  <div class="title-band"><h1>Page title goes here</h1></div>
  <div class="title-fade"></div>

  <ul class="side-nav">
    <li>Product category one</li>
    <li>Product category two</li>
    <li class="active">Product category three</li>
    <li>Product category four</li>
    <li>Product category five</li>
    <li>Product category six</li>
  </ul>

  <main class="content">
    <p>Lorem ipsum dolor sit amet, consectetur adipiscing elit. Pellentesque justo arcu, ultrices nec tincidunt ut, tempus ac felis. Vestibulum ante ipsum primis in faucibus orci luctus et ultrices posuere cubilia Curae; <a class="link" href="#">Donec sed massa sem</a> ut venenatis dui. Nullam ullamcorper lacus vel magna dignissim egestas. Sed sit amet velit a dolor sodales cursus. Sed convallis, urna tristique feugiat gravida, lectus libero vehicula erat, quis venenatis libero urna quis nunc. Nunc id tellus eget odio luctus molestie</p>
    <h2>Lorem ipsum dolar sit</h2>
    <p>Vestibulum in tellus tortor. Proin lorem urna, dignissim et facilisis aliquet, pharetra eu augue. Morbi pellentesque porttitor neque, vitae posuere risus faucibus ut. In hac habitasse platea dictumst. Ut ut nunc turpis. Donec non mi nisl. Donec nisl risus, pulvinar in ornare et, tincidunt vitae massa.</p>
    <ul>
      <li>Lorem ipsum dolar sit luctus non vulputate in, adipiscing eget ligula</li>
      <li>Phasellus diam turpis luctus non vulputate in, adipiscing eget ligula</li>
      <li>Luctus non vulputate in, adipiscing eget ligula</li>
    </ul>
    <p>In quis diam ac justo tempor pretium eu elementum tellus. Morbi eget dui ut ante ornare pulvinar. Sed dictum mattis felis, a dictum leo scelerisque sed. Quisque egestas, velit sed condimentum auctor, diam nulla tempus metus, a convallis nisi elit non ipsum. Phasellus vehicula rhoncus erat, sed viverra dolor consectetur vel.</p>
  </main>

  <aside class="aside">
    <div class="photo" role="img" aria-label="Photo of children blowing soap bubbles outdoors in sunlight"></div>
    <div class="enlarge">
      <svg width="13" height="13" viewBox="0 0 13 13" aria-hidden="true"><circle cx="5.5" cy="5.5" r="4.5" fill="none" stroke="#777" stroke-width="1.6"/><path d="M9 9l3.5 3.5M3.5 5.5h4M5.5 3.5v4" stroke="#777" stroke-width="1.6"/></svg>
      enlarge image
    </div>
    <div class="rule"></div>
    <h3>Subscribe</h3>
    <p class="intro">Lorem ipsum dolor sit amet, consectetur adipiscing elit. Vivamus ...</p>
    <input class="field name" type="text" placeholder="Enter your name">
    <input class="field email" type="text" placeholder="Enter your e-mail address">
    <a href="#" class="btn-subscribe">Subscribe</a>
  </aside>

  <div class="footer-rule"></div>

  <div class="footer-col" style="left:68px">
    <h4>Customer Service</h4>
    <ul>
      <li><svg width="9" height="8" viewBox="0 0 9 8" aria-hidden="true"><path d="M0 4h8M5 1l3 3-3 3" fill="none" stroke="#999" stroke-width="1.2"/></svg>Contact Us.</li>
      <li><svg width="9" height="8" viewBox="0 0 9 8" aria-hidden="true"><path d="M0 4h8M5 1l3 3-3 3" fill="none" stroke="#999" stroke-width="1.2"/></svg>Frequently Asked Questions.</li>
      <li><svg width="9" height="8" viewBox="0 0 9 8" aria-hidden="true"><path d="M0 4h8M5 1l3 3-3 3" fill="none" stroke="#999" stroke-width="1.2"/></svg>Return Policy Information.</li>
    </ul>
  </div>
  <div class="footer-col" style="left:349px">
    <h4>My Account</h4>
    <ul>
      <li><svg width="9" height="8" viewBox="0 0 9 8" aria-hidden="true"><path d="M0 4h8M5 1l3 3-3 3" fill="none" stroke="#999" stroke-width="1.2"/></svg>Login/Register.</li>
      <li><svg width="9" height="8" viewBox="0 0 9 8" aria-hidden="true"><path d="M0 4h8M5 1l3 3-3 3" fill="none" stroke="#999" stroke-width="1.2"/></svg>My Account.</li>
      <li><svg width="9" height="8" viewBox="0 0 9 8" aria-hidden="true"><path d="M0 4h8M5 1l3 3-3 3" fill="none" stroke="#999" stroke-width="1.2"/></svg>Order Status</li>
    </ul>
  </div>

  <div class="contact" style="left:641px">Phone: 000 000 000<br>Fax:&nbsp;&nbsp;&nbsp;&nbsp; 000 000 000<br>info@corvanelkids.com</div>
  <div class="contact" style="left:852px">Address detals<br>Address details<br>Country</div>

  <div class="footer-brand">corvanelkids</div>

  <div class="legal">© 2010 Copyright Corvanel Kids</div>
  <nav class="footer-nav">
    <a href="#">Home</a><span class="sep">|</span><a href="#">About us</a><span class="sep">|</span><a href="#">Services</a><span class="sep">|</span><a href="#">Products</a><span class="sep">|</span><a href="#">News</a><span class="sep">|</span><a href="#">Sitemap</a><span class="sep">|</span><a href="#">Contact us</a>
  </nav>
  <div class="social" aria-label="Social links"><span></span><span></span><span></span><span></span><span></span><span></span></div>
</div>
</body>
</html>
```